vBRIDGE ON LLC - New Website Design Help!

Need to build a website that showcases our capabilities. We will be specializing in Government Contracting for SDVOSB set aside and sole source contracts. We provide many services such as Audio & Visual design, install, consulting, all the way through to project completion. Also, IT/Voice infrastructure consulting, design, implementation, project management all the way to project completion.

Target Market(s)

IT/Voice Government Contracts, Managed Service Contracts for Government

Industry/Entity Type

Information Technology and Telecommunications

Coding

Coded - Design and coding required

Number of Pages Required

5+ page

Font styles to use
Other font styles liked:
• Calibri

Colors

Designer to choose only greyscale colors for use in the design.

Requirements
Must have
• Drop downs for additional pages, for About Us, Services, Industry Solutions, Our Company, Contact Us
Nice to have
• Testimonials page or Blog page

```html
<!DOCTYPE html>
<html lang="en">
<head>
<meta charset="utf-8">
<title>vBRIDGE ON LLC – Government Contracting for SDVOSB</title>
<link href="https://fonts.googleapis.com/css2?family=Poppins:wght@400;500;600;700&family=Montserrat:wght@400;500;600&family=Open+Sans:wght@400;500&display=swap" rel="stylesheet">
<style>
:root{
  --black:#111111;
  --ink:#1c1c1c;
  --text:#444444;
  --muted:#8a8a8a;
  --grey:#d8d8d8;
  --grey-mid:#7a7a7a;
  --light:#efefef;
  --white:#ffffff;
  --button:#1e1e1e;
  --star:#b8c400;
}
*{box-sizing:border-box;margin:0;padding:0}
html,body{width:1200px;height:4654px;overflow:hidden}
body{position:relative;font-family:"Montserrat",sans-serif;color:var(--ink);background:var(--white)}
.abs{position:absolute}
.btn{position:absolute;display:flex;align-items:center;justify-content:center;font-family:"Montserrat",sans-serif;font-weight:500;font-size:15px;letter-spacing:.3px;color:var(--white);background:var(--button)}
.btn.grey{background:var(--grey-mid)}
h2.section-title{position:absolute;font-family:"Poppins",sans-serif;font-weight:600;font-size:38px;color:var(--ink);letter-spacing:.3px}

/* top bar */
.topbar{left:0;top:0;width:1200px;height:85px;background:var(--black)}
.brand{position:absolute;left:24px;top:18px;height:48px;display:flex;align-items:center;gap:10px;font-family:"Poppins",sans-serif;font-weight:600;font-size:30px;color:var(--white);letter-spacing:1px}
.brand .mark{width:22px;height:22px;background:var(--white)}
.toplink{position:absolute;top:38px;font-size:15px;font-weight:500;color:var(--white)}
.search{position:absolute;left:730px;top:31px;width:172px;height:30px;background:var(--white);font-size:13px;color:#b0b0b0;padding:7px 12px}
.search-btn{position:absolute;left:902px;top:31px;width:50px;height:30px;background:var(--grey-mid)}
.social{position:absolute;top:36px;width:20px;height:20px;border-radius:50%;background:var(--white)}

/* nav */
.nav{left:0;top:85px;width:1200px;height:51px;background:var(--white)}
.nav a{position:absolute;top:18px;font-size:14px;font-weight:500;color:var(--ink);text-decoration:none}
.nav .btn{left:987px;top:8px;width:171px;height:34px;background:var(--grey-mid);font-size:14px}

/* hero */
.hero{left:0;top:136px;width:1200px;height:556px;background:linear-gradient(90deg,#2e2e2e 0%,#4a4a4a 45%,#6f6660 70%,#3a3a3a 100%)}
.hero h1{position:absolute;left:34px;top:118px;width:620px;font-family:"Poppins",sans-serif;font-weight:700;font-size:45px;line-height:53px;color:var(--white)}
.hero p{position:absolute;left:34px;top:290px;width:600px;font-size:14px;line-height:26px;color:var(--white)}
.hero .btn{left:32px;top:390px;width:172px;height:32px;background:var(--grey-mid)}

/* grey area */
.grey-area{left:0;top:692px;width:1200px;height:1455px;background:var(--grey)}
.stats{left:193px;top:645px;width:794px;height:165px;background:var(--light)}
.stat{position:absolute;top:44px;display:flex;align-items:flex-start;gap:14px}
.stat .num{font-family:"Poppins",sans-serif;font-weight:600;font-size:52px;line-height:56px;color:var(--ink)}
.stat .lbl{font-size:14px;color:var(--muted)}

.about-photo{left:34px;top:904px;width:532px;height:368px;background:linear-gradient(135deg,#9a9a9a,#5e5e5e 55%,#8c8780)}
.about h2{position:absolute;left:625px;top:956px;font-family:"Poppins",sans-serif;font-weight:600;font-size:38px}
.about p{position:absolute;left:631px;width:500px;font-size:12.5px;line-height:23px;color:var(--text)}
.about .btn{left:631px;top:1193px;width:211px;height:32px}

.partners{left:34px;top:1354px;width:1126px;height:122px;background:var(--light)}
.partner{position:absolute;top:44px;height:34px;background:#b9b9b9}

.service{position:absolute;width:300px}
.service svg{display:block;margin-bottom:18px}
.service h3{font-family:"Poppins",sans-serif;font-weight:500;font-size:25px;color:var(--ink);margin-bottom:12px}
.service p{font-size:11.5px;line-height:20px;color:var(--muted)}

/* expert solutions */
.expert{left:0;top:2147px;width:1200px;height:713px;background:var(--light)}
.tiles{position:absolute;left:94px;top:189px;width:1008px;height:449px;display:grid;grid-template-columns:repeat(3,336px);grid-template-rows:repeat(2,224.5px)}
.tile{position:relative}
.tile span{position:absolute;left:16px;bottom:12px;font-family:"Open Sans",sans-serif;font-size:23px;line-height:32px;color:var(--white)}
.tile.cta{background:linear-gradient(180deg,#1e3a5f 0 58%,#7b7b7b 58%)}
.tile.cta span{color:#e6e6e6}

/* testimonials */
.testimonials{left:0;top:2860px;width:1200px;height:555px;background:var(--grey)}
.card{position:absolute;top:179px;width:237px;height:246px;background:var(--white);border-radius:20px;text-align:center}
.card .avatar{width:58px;height:58px;border-radius:50%;background:linear-gradient(135deg,#8d8d8d,#4b4b4b);margin:14px auto 10px}
.card h4{font-size:16px;font-weight:500}
.card p{margin:14px auto 0;width:180px;font-size:11px;line-height:17px;color:var(--text)}
.card .stars{margin-top:10px;font-size:22px;letter-spacing:4px;color:var(--star)}

/* blog */
.blog{left:0;top:3415px;width:1200px;height:546px;background:#f2f2f2}
.blog h2{position:absolute;left:74px;top:68px;font-family:"Poppins",sans-serif;font-weight:600;font-size:37px}
.blog .btn{left:950px;top:60px;width:174px;height:33px;background:var(--black)}
.post{position:absolute;top:154px;width:224px;height:316px;background:var(--white);border:1px solid #d0d0d0;text-align:center}
.post .thumb{height:159px;background:linear-gradient(135deg,#c8c8c8,#7c7c7c)}
.post h5{margin-top:30px;font-size:14px;font-weight:600}
.post p{margin:14px auto 0;width:186px;font-size:8.5px;line-height:14px;color:var(--text);text-transform:uppercase}
.post .more{margin-top:14px;font-size:10px;font-weight:600;color:var(--text)}

/* cta */
.cta-band{left:0;top:3961px;width:1200px;height:267px;background:var(--grey)}
.cta-band h2{position:absolute;left:84px;top:110px;font-family:"Poppins",sans-serif;font-weight:600;font-size:43px}
.cta-band p{position:absolute;left:84px;top:180px;width:520px;font-size:13.5px;line-height:25px;color:var(--text)}
.cta-band .btn{left:857px;top:139px;width:216px;height:33px;background:var(--black)}

/* footer */
.footer{left:0;top:4228px;width:1200px;height:426px;background:var(--black);color:var(--white)}
.footer .brand{left:60px;top:82px}
.footer h6{position:absolute;top:86px;font-family:"Poppins",sans-serif;font-weight:400;font-size:24px;color:#a8a8a8}
.footer ul{position:absolute;top:144px;list-style:none}
.footer li{font-size:17px;height:37px;display:flex;align-items:center;gap:12px}
.contact-line{position:absolute;left:60px;display:flex;align-items:center;gap:16px;font-size:15px}
.newsletter{position:absolute;left:882px;top:148px;width:174px;height:32px;background:var(--white);font-size:12px;color:#a0a0a0;padding:9px 10px}
.newsletter-btn{position:absolute;left:1056px;top:148px;width:52px;height:32px;background:var(--grey-mid);font-size:13px;display:flex;align-items:center;justify-content:center}
.footer .dot{position:absolute;top:234px;width:26px;height:26px;border-radius:50%;background:#d0d0d0}
.copyright{position:absolute;top:386px;font-size:14px}
</style>
</head>
<body>

<header class="abs topbar">
  <div class="brand"><span class="mark"></span>vBRIDGE ON</div>
  <span class="toplink" style="left:358px">Customer Portal</span>
  <span class="toplink" style="left:537px">Support Center</span>
  <div class="search">Search Here</div>
  <div class="search-btn"></div>
  <span class="social" style="left:1048px"></span>
  <span class="social" style="left:1085px"></span>
  <span class="social" style="left:1124px"></span>
</header>

<nav class="abs nav">
  <a style="left:27px">HOME</a>
  <a style="left:117px">ABOUT US</a>
  <a style="left:239px">SERVICES</a>
  <a style="left:367px">INDUSTRY SOLUTIONS</a>
  <a style="left:582px">OUR COMPANY</a>
  <a style="left:743px">TESTIMONIALS</a>
  <a style="left:898px">BLOG</a>
  <span class="btn">CONTACT US</span>
</nav>

<section class="abs hero" role="img" aria-label="Photo of a smiling professional in an office">
  <h1>We Are Specializing in Government Contracting for SDVOSB</h1>
  <p>Lorem ipsum dolor sit amet, consectetur adipiscing elit, sed do eiusmod tempor incididunt ut labore et dolore magna aliqua. Ut enim ad minim veniam, quis nostrud exercitation ullamco laboris nisi ut aliquip ex ea commodo consequat.</p>
  <span class="btn">CONTACT US</span>
</section>

<section class="abs grey-area"></section>

<div class="abs stats">
  <div class="stat" style="left:36px">
    <svg width="70" height="80" viewBox="0 0 70 80" fill="none" stroke="#666" stroke-width="2"><circle cx="35" cy="32" r="24"/><circle cx="35" cy="32" r="15"/><path d="M22 52 14 76l10-5 6 8 5-18M48 52l8 24-10-5-6 8-5-18"/></svg>
    <div><div class="num">20+</div><div class="lbl">Years Of Experience</div></div>
  </div>
  <div class="stat" style="left:296px">
    <svg width="72" height="70" viewBox="0 0 72 70" fill="none" stroke="#666" stroke-width="2"><circle cx="36" cy="14" r="8"/><circle cx="16" cy="26" r="7"/><circle cx="56" cy="26" r="7"/><circle cx="36" cy="40" r="8"/><path d="M4 56c0-10 24-10 24 0M44 56c0-10 24-10 24 0M20 68c0-12 32-12 32 0"/></svg>
    <div><div class="num">500+</div><div class="lbl">Customers</div></div>
  </div>
  <div class="stat" style="left:562px">
    <svg width="72" height="74" viewBox="0 0 72 74" fill="none" stroke="#666" stroke-width="2"><path d="M6 40 26 20l14 10 14-12 12 14-20 22-12-8-12 14z"/><path d="M20 8v8M34 4v8M48 8v6"/></svg>
    <div><div class="num">98%</div><div class="lbl">Success Score</div></div>
  </div>
</div>

<div class="abs about-photo" role="img" aria-label="Photo of two colleagues working at a laptop in a meeting room"></div>
<div class="about">
  <h2>ABOUT US</h2>
  <p style="top:1020px">Lorem ipsum dolor sit amet, consectetur adipiscing elit, sed do eiusmod tempor incididunt ut labore et dolore magna aliqua. Ut enim ad minim veniam, quis nostrud exercitation ullamco laboris nisi ut aliquip ex ea commodo consequat.</p>
  <p style="top:1101px">Lorem ipsum dolor sit amet, consectetur adipiscing elit, sed do eiusmod tempor incididunt ut labore et dolore magna aliqua. Ut enim ad minim veniam, quis nostrud exercitation ullamco laboris nisi ut aliquip ex ea commodo consequat.</p>
  <span class="btn">ABOUT OUR COMPANY</span>
</div>

<div class="abs partners" aria-label="Partner badges">
  <span class="partner" style="left:18px;width:140px"></span>
  <span class="partner" style="left:202px;width:140px"></span>
  <span class="partner" style="left:388px;width:140px"></span>
  <span class="partner" style="left:572px;width:140px"></span>
  <span class="partner" style="left:766px;width:130px"></span>
  <span class="partner" style="left:944px;width:146px;height:58px;top:32px"></span>
</div>

<div class="service" style="left:54px;top:1566px">
  <svg width="76" height="70" viewBox="0 0 76 70" fill="none" stroke="#666" stroke-width="2"><rect x="4" y="4" width="68" height="46" rx="2"/><rect x="12" y="12" width="52" height="30"/><path d="M30 50v10M46 50v10M22 64h32"/></svg>
  <h3>Audio &amp; Visual design</h3>
  <p>Lorem ipsum dolor sit amet, consectetur adipiscing elit, sed do eiusmod tempor incididunt ut labore et dolore magna aliqua.</p>
</div>
<div class="service" style="left:445px;top:1566px">
  <svg width="86" height="76" viewBox="0 0 86 76" fill="none" stroke="#666" stroke-width="2"><circle cx="40" cy="38" r="30"/><circle cx="40" cy="38" r="16"/><circle cx="64" cy="60" r="12"/><path d="m58 60 5 5 8-9"/></svg>
  <h3 style="font-size:24px">INSTALLATION&nbsp; SERVICES</h3>
  <p>Lorem ipsum dolor sit amet, consectetur adipiscing elit, sed do eiusmod tempor incididunt ut labore et dolore magna aliqua.</p>
</div>
<div class="service" style="left:838px;top:1566px">
  <svg width="86" height="76" viewBox="0 0 86 76" fill="none" stroke="#666" stroke-width="2"><circle cx="30" cy="30" r="12"/><path d="M16 30a14 14 0 0 1 28 0M6 74V56a10 10 0 0 1 10-10h28a10 10 0 0 1 10 10v18z"/><rect x="50" y="4" width="30" height="20" rx="4"/><path d="M56 12h18M56 18h12"/></svg>
  <h3>24/7 Support</h3>
  <p>Lorem ipsum dolor sit amet, consectetur adipiscing elit, sed do eiusmod tempor incididunt ut labore et dolore magna aliqua.</p>
</div>
<div class="service" style="left:54px;top:1810px">
  <svg width="70" height="72" viewBox="0 0 70 72" fill="none" stroke="#666" stroke-width="2"><rect x="10" y="4" width="44" height="64"/><rect x="20" y="14" width="24" height="44"/><circle cx="32" cy="34" r="5"/><path d="M32 39v8M4 68h62"/></svg>
  <h3>Access Control</h3>
  <p>Lorem ipsum dolor sit amet, consectetur adipiscing elit, sed do eiusmod tempor incididunt ut labore et dolore magna aliqua.</p>
</div>
<div class="service" style="left:445px;top:1810px">
  <svg width="76" height="72" viewBox="0 0 76 72" fill="none" stroke="#666" stroke-width="2"><circle cx="26" cy="44" r="20"/><path d="M14 62 8 70l12-4"/><path d="M38 20a18 18 0 1 1 24 24l6 8-12-4"/><path d="M50 22h14M50 28h14M50 34h10"/><path d="M22 40a4 4 0 1 1 5 4v4M27 54v1"/></svg>
  <h3>Consulting</h3>
  <p>Lorem ipsum dolor sit amet, consectetur adipiscing elit, sed do eiusmod tempor incididunt ut labore et dolore magna aliqua.</p>
</div>
<div class="service" style="left:838px;top:1810px">
  <svg width="76" height="72" viewBox="0 0 76 72" fill="none" stroke="#666" stroke-width="2"><rect x="4" y="4" width="50" height="64"/><path d="M12 16h8v8h-8zM26 20h20M12 34h8v8h-8zM26 38h20"/><rect x="34" y="44" width="38" height="26"/><path d="M42 52h6v6h-6zM56 52h6v6h-6z"/></svg>
  <h3>Project Management</h3>
  <p>Lorem ipsum dolor sit amet, consectetur adipiscing elit, sed do eiusmod tempor incididunt ut labore et dolore magna aliqua.</p>
</div>
<span class="btn grey" style="left:497px;top:2054px;width:172px;height:33px">CONTACT US</span>

<section class="abs expert">
  <h2 class="section-title" style="left:0;width:1200px;text-align:center;top:76px">EXPERT SOLUTIONS</h2>
  <div class="tiles">
    <div class="tile" role="img" aria-label="Business team in a blue-toned office" style="background:linear-gradient(180deg,#3d6a93,#1f3f60)"><span>Enhanced visibility</span></div>
    <div class="tile" role="img" aria-label="Professional viewing data screens in a control room" style="background:linear-gradient(180deg,#2a4a6c,#1d3552)"><span>Informed decisions</span></div>
    <div class="tile" role="img" aria-label="Person looking over a city skyline" style="background:linear-gradient(180deg,#8a99a8,#2f4c6c)"><span>New business wins</span></div>
    <div class="tile" role="img" aria-label="Hand using a digital security interface" style="background:linear-gradient(180deg,#5f7a92,#1f3a58)"><span>Real time performance<br>measurement</span></div>
    <div class="tile" role="img" aria-label="Financial charts and graphs on screens" style="background:linear-gradient(135deg,#7a3a40,#2b3c66 60%,#1c3050)"><span>Increased profitability</span></div>
    <div class="tile cta" role="img" aria-label="Glowing digital network globe"><span>View our solutions<br>&amp; services</span></div>
  </div>
</section>

<section class="abs testimonials">
  <h2 class="section-title" style="left:0;width:1200px;text-align:center;top:80px">TESTIMONIALS</h2>
  <div class="card" style="left:179px"><div class="avatar" role="img" aria-label="Client portrait"></div><h4>John Doe</h4><p>Lorem ipsum dolor sit amet, consectetur adipiscing elit, sed do eiusmod tempor incididunt ut labore et dolore magna aliqua.</p><div class="stars">★★★★★</div></div>
  <div class="card" style="left:479px"><div class="avatar" role="img" aria-label="Client portrait"></div><h4>John Doe</h4><p>Lorem ipsum dolor sit amet, consectetur adipiscing elit, sed do eiusmod tempor incididunt ut labore et dolore magna aliqua.</p><div class="stars">★★★★★</div></div>
  <div class="card" style="left:779px"><div class="avatar" role="img" aria-label="Client portrait"></div><h4>John Doe</h4><p>Lorem ipsum dolor sit amet, consectetur adipiscing elit, sed do eiusmod tempor incididunt ut labore et dolore magna aliqua.</p><div class="stars">★★★★★</div></div>
</section>

<section class="abs blog">
  <h2>LATEST FROM BLOG</h2>
  <span class="btn">VIEW ALL</span>
  <article class="post" style="left:83px"><div class="thumb" role="img" aria-label="Colleagues reviewing work at a laptop"></div><h5>BLOG POST 1</h5><p>How we plan secure voice networks for federal sites from survey to final handoff.</p><div class="more">READ MORE ⟶</div></article>
  <article class="post" style="left:358px"><div class="thumb" role="img" aria-label="Professional smiling in an office"></div><h5>BLOG POST 2</h5><p>Key steps to winning set aside contracts as a small veteran owned business.</p><div class="more">READ MORE ⟶</div></article>
  <article class="post" style="left:633px"><div class="thumb" role="img" aria-label="Professional working on a laptop"></div><h5>BLOG POST 3</h5><p>Choosing audio and visual systems that scale with growing agency teams.</p><div class="more">READ MORE ⟶</div></article>
  <article class="post" style="left:908px"><div class="thumb" role="img" aria-label="Team meeting around a desk"></div><h5>BLOG POST 4</h5><p>Managed service contracts and what they mean for uptime.</p><div class="more">READ MORE ⟶</div></article>
</section>

<section class="abs cta-band">
  <h2>24/7 Service and Support!</h2>
  <p>Lorem ipsum dolor sit amet, consectetur adipiscing elit, sed do eiusmod tempor incididunt ut labore et dolore magna aliqua.</p>
  <span class="btn">CONTACT US NOW</span>
</section>

<footer class="abs footer">
  <div class="brand"><span class="mark"></span>vBRIDGE ON</div>
  <div class="contact-line" style="top:190px"><svg width="20" height="20" viewBox="0 0 24 24" fill="#bbb"><path d="M6.6 10.8a15 15 0 0 0 6.6 6.6l2.2-2.2a1 1 0 0 1 1-.25 11 11 0 0 0 3.6.6 1 1 0 0 1 1 1V20a1 1 0 0 1-1 1A17 17 0 0 1 3 4a1 1 0 0 1 1-1h3.5a1 1 0 0 1 1 1 11 11 0 0 0 .6 3.6 1 1 0 0 1-.25 1z"/></svg>(+1) 555 014 2290</div>
  <div class="contact-line" style="top:240px"><svg width="20" height="18" viewBox="0 0 24 20" fill="#bbb"><path d="M2 6l10 6 10-6v12H2z"/><path d="M2 4h20l-10 6z"/></svg>support@vbridgeon.com</div>
  <div class="contact-line" style="top:288px"><svg width="20" height="22" viewBox="0 0 24 26" fill="#bbb"><path d="M12 1a8 8 0 0 0-8 8c0 6 8 16 8 16s8-10 8-16a8 8 0 0 0-8-8zm0 11a3 3 0 1 1 0-6 3 3 0 0 1 0 6z"/></svg>418 Harbor Ridge Rd, Suite 12</div>

  <h6 style="left:380px">QUICK LINKS</h6>
  <ul style="left:380px"><li>›&nbsp;HOME</li><li>›&nbsp;ABOUT</li><li>›&nbsp;SERVICES</li><li>›&nbsp;PROJECTS</li><li>›&nbsp;CONTACT</li></ul>
  <h6 style="left:638px">SERVICES</h6>
  <ul style="left:638px"><li>›&nbsp;SERVICE 1</li><li>›&nbsp;SERVICE 2</li><li>›&nbsp;SERVICES</li><li>›&nbsp;SERVICE 4</li><li>›&nbsp;SERVICE 5</li></ul>
  <h6 style="left:882px">NEWSLETTER</h6>
  <div class="newsletter">Email Address</div>
  <div class="newsletter-btn">SEND</div>
  <span class="dot" style="left:882px"></span>
  <span class="dot" style="left:927px"></span>
  <span class="dot" style="left:973px"></span>

  <div class="copyright" style="left:54px">© 2024 | All Rights Reserved.</div>
  <div class="copyright" style="left:849px">Terms &amp; Conditions | Privacy Policy</div>
</footer>

</body>
</html>
```